Leaflet design to advertise new event management system

We are a software company based in Greater London and are in need of a leaflet design to advertise 'Velturo'- a new event competition management system.
The leaflet will be distributed around event competitions (such as flower shows or kids competitions) to market the product and pick up prospective clients.
Velturo is easy and simple, and we would like the design to reflect that.
We would like to see designs which use our orange #f05f40
Please see attached for a rough example of what we are hoping for and visit www.velturo-example.com for more inspiration.

Industry/Entity Type

It Company

```html
<!DOCTYPE html>
<html lang="en">
<head>
<meta charset="utf-8">
<title>Velturo – Event competition management made simple</title>
<link rel="stylesheet" href="https://fonts.googleapis.com/css2?family=Quicksand:wght@300;400;500;700&family=Roboto+Condensed:wght@700&display=swap">
<style>
:root{
  --orange:#f05f40;
  --frame:#f3876f;
  --ink:#4a4548;
  --grey:#6b6769;
  --white:#ffffff;
  --paper:#ffffff;
  --grass:#7fae52;
  --coat:#34343a;
}
*{margin:0;padding:0;box-sizing:border-box}
html,body{width:1200px;height:846px;overflow:hidden;background:var(--paper)}
.leaflet{position:relative;width:1200px;height:846px;font-family:"Quicksand",sans-serif;color:var(--ink)}
.hero{position:absolute;left:12px;top:12px;width:1176px;height:395px;border:5px solid var(--frame);border-radius:22px;overflow:hidden}
.hero-photo{position:absolute;inset:0;background:linear-gradient(100deg,var(--grass) 0%,#5d7d48 35%,var(--coat) 60%,#4b5a40 100%)}
.brand{position:absolute;right:22px;top:30px;font-family:"Roboto Condensed",sans-serif;font-weight:700;font-size:96px;line-height:1;color:var(--orange);letter-spacing:1px}
.quote{position:absolute;left:575px;top:170px;width:400px;text-align:center;color:var(--white);font-weight:700;font-size:27px;line-height:36px}
.headline{position:absolute;left:0;top:403px;width:1200px;text-align:center;font-weight:300;font-size:56px;letter-spacing:.5px;color:var(--ink)}
.intro{position:absolute;left:0;top:474px;width:1200px;text-align:center;font-size:22.5px;color:var(--orange);font-weight:400}
.features{position:absolute;left:69px;top:515px;display:flex;gap:8px}
.feature{width:261px;height:188px;background:var(--orange);border-radius:20px;color:var(--white);text-align:center;padding:9px 17px 0}
.feature h2{font-size:22px;font-weight:700;text-decoration:underline;text-underline-offset:4px;text-decoration-thickness:2px;margin-bottom:24px;letter-spacing:.1px;white-space:nowrap}
.feature p{font-size:21px;font-weight:400;line-height:27px}
.call{position:absolute;left:0;top:700px;width:1200px;text-align:center;font-weight:700;font-size:56px;color:var(--ink);letter-spacing:.5px}
.email{position:absolute;left:0;top:756px;width:1200px;text-align:center;font-size:30px;color:var(--grey);font-weight:400}
.categories{position:absolute;left:0;top:794px;width:1200px;height:52px;background:var(--orange);display:flex;align-items:center;justify-content:center;list-style:none;color:var(--white);font-weight:700;font-size:22px}
.categories li{padding:0 23px}
.categories li+li{border-left:1px solid rgba(255,255,255,.6)}
</style>
</head>
<body>
<main class="leaflet">
  <section class="hero">
    <div class="hero-photo" role="img" aria-label="Photo of a black and white collie leaping over an agility jump on green grass"></div>
    <div class="brand">VELTURO</div>
    <p class="quote">“Having a livestream has made publishing our event results so much easier.”</p>
  </section>
  <h1 class="headline">Event competition management made simple</h1>
  <p class="intro">Velturo has everything you need to get your event competition up and running in no time!</p>
  <div class="features">
    <article class="feature"><h2>EVENT TEMPLATES</h2><p>Build one or more competition templates for repeating events.</p></article>
    <article class="feature"><h2>YOUR COMPETITIONS</h2><p>Competition sections, categories and classes keep your lupins from your Victoria sponges</p></article>
    <article class="feature"><h2>ONLINE ENTRY</h2><p>Invite your competitors to sign</p></article>
    <article class="feature"><h2>INSTANT RESULTS</h2><p>Publish your competition results straight to the web!</p></article>
  </div>
  <p class="call">CALL 0845 555 0192</p>
  <p class="email">hello@velturo-example.com</p>
  <ul class="categories">
    <li>CAKES AND BAKING</li>
    <li>FLOWERS AND ARRANGEMENTS</li>
    <li>PHOTOGRAPHY ARTS AND CRAFTS</li>
  </ul>
</main>
</body>
</html>
```